■依頼の目的/概要

当社は、宮城県仙台市にて、新築・リフォーム事業を行っている会社です。
女性に好まれるようなサイトデザインにしたく、今回、制作依頼致します。

■ホームページ内容

TOPページ / リフォーム事例 / お問合せ 合計3ページ

■重視する点/検討基準

・女性(主婦)に好まれるようなデザイン
・リフォームを相談したくなる
・楽しそうな夢を叶えてくれそうな…
・素人目線でのアイディア・ご提案コンテンツがあれば尚可

■ご質問

その他、疑問点がありましたら、お気軽にご質問ください。
株式会社 みのり舎 http://www.minori-sha.co.jp/
デザイナーさんの能力を十分に発揮して頂きたいので、
納品ファイル形式は、限定しておりませんでしたが、
好ましい形式を記載致します。

html、css、それに関連する画像ファイル。
Flash 、JavaScriptなども使用可。
フォトショップ形式、イラストレーター形式。
コーディング無しの全3ページのサイトデザイン。

マル写真と家のイラストで、やわらかいイメージを与える。
トップページを見ただけで、会社の特徴がわかる。

この度は、皆様に多くのご提案して頂きまして、誠にありがとうございました。それぞれのご提案に良い点があり、一人の方に選択するのが、難航をし、また、大変心苦しかったです。
また、何かありましたら、ご提案して頂けましたら幸いです。
今後とも、何卒、よろしくお願い致します。

```html
<!DOCTYPE html>
<html lang="ja">
<head>
<meta charset="utf-8">
<title>株式会社 みのり舎</title>
<link rel="stylesheet" href="https://fonts.googleapis.com/css2?family=M+PLUS+Rounded+1c:wght@400;700&family=Noto+Sans+JP:wght@400;700&display=swap">
<style>
:root{
  --rose:#c4506b;
  --rose-soft:#e9b7c3;
  --rose-pale:#f8e8ec;
  --ink:#4a4040;
  --ink-soft:#8a7f7c;
  --line:#ddd3cf;
  --paper:#ffffff;
  --bg:#f4f0ec;
  --beige:#efe7de;
  --wood:#c9a987;
  --wood-light:#ead9c5;
  --green:#9bb07a;
}
*{box-sizing:border-box;margin:0;padding:0}
html,body{width:667px;height:1200px;overflow:hidden}
body{background:var(--bg);font-family:"Noto Sans JP",sans-serif;color:var(--ink);font-size:9px;line-height:1.4}
.page{width:543px;margin:0 auto;background:var(--paper);height:1200px;position:relative}
.header{height:46px;display:flex;justify-content:space-between;align-items:center;padding:0 8px}
.brand{display:flex;align-items:center;gap:6px}
.brand-mark{width:22px;height:22px;border-radius:50%;background:var(--rose)}
.brand-tag{font-size:6px;color:var(--ink-soft)}
.brand-name{font-family:"M PLUS Rounded 1c",sans-serif;font-weight:700;font-size:15px;color:var(--ink)}
.contact-top{text-align:right}
.util{display:flex;gap:3px;justify-content:flex-end;margin-bottom:2px}
.util span{background:var(--rose);color:#fff;font-size:6px;padding:1px 5px;border-radius:2px}
.util span+span{background:var(--ink-soft)}
.tel{display:flex;align-items:center;gap:3px;justify-content:flex-end;font-family:"M PLUS Rounded 1c",sans-serif;font-weight:700;font-size:17px;color:var(--rose);line-height:1}
.tel-hours{font-size:6px;color:var(--ink-soft)}
.nav{display:flex;height:30px;border-top:1px solid var(--line);border-bottom:3px solid var(--rose);background:linear-gradient(#fff,#f3eeea)}
.nav a{flex:1;text-align:center;text-decoration:none;color:var(--ink);font-size:8px;font-weight:700;padding-top:5px;border-right:1px solid var(--line)}
.nav a small{display:block;font-size:5px;color:var(--ink-soft);font-weight:400}
.nav a.current{color:var(--rose)}
.hero{height:172px;margin-top:4px;position:relative;display:flex}
.hero-photo{flex:1;background:linear-gradient(120deg,#f2ebe2 0%,#e3d3c0 45%,#c9ab8b 100%)}
.hero-band{position:absolute;left:244px;top:0;width:54px;height:172px;background:rgba(196,80,107,.88);color:#fff;writing-mode:vertical-rl;font-family:"M PLUS Rounded 1c",sans-serif;display:flex;align-items:center;justify-content:center;gap:6px;padding:10px 0}
.hero-band .lead{font-size:15px;font-weight:700;letter-spacing:2px}
.hero-band .sub{font-size:9px;letter-spacing:2px}
.body{display:flex;gap:10px;padding:8px 0 0}
.main{width:393px}
.side{width:140px}
.sec-head{display:flex;justify-content:space-between;align-items:center;height:18px;border-bottom:1px solid var(--line);border-left:4px solid var(--rose);padding-left:6px;background:linear-gradient(90deg,#f6f1ee,#fff);margin-bottom:8px}
.sec-head h2{font-size:10px;font-weight:700}
.sec-head span{font-size:6px;color:var(--rose);padding-right:4px}
.type-grid{display:grid;grid-template-columns:190px 190px;gap:10px 13px;margin-bottom:12px}
.type-card{border:1px solid var(--line);padding:4px;height:104px;display:flex;flex-direction:column;box-shadow:0 1px 2px rgba(0,0,0,.06)}
.type-card h3{font-size:9px;text-align:center;font-weight:700;height:16px}
.type-card .photo{height:68px;margin:0 auto;width:110px}
.type-card .more{font-size:6px;color:var(--rose);text-align:right;margin-top:auto}
.ph-house{background:linear-gradient(135deg,#f3ede6,#d9c4ab)}
.ph-mansion{background:linear-gradient(135deg,#f7f3ee,#e0d2c6)}
.ph-new{background:linear-gradient(160deg,#dde6ef,#f4f2ee 60%,#cbb9a4)}
.ph-shop{background:linear-gradient(135deg,#c8a27a,#8a6448)}
.part-list{display:grid;grid-template-columns:190px 190px;gap:4px 13px;list-style:none;margin-bottom:12px}
.part-list li{height:19px;border:1px solid var(--line);background:linear-gradient(#fff,#f7f3f0);display:flex;align-items:center;padding-left:6px;font-size:7.5px;font-weight:700}
.part-list li::before{content:"";width:0;height:0;border-left:4px solid var(--rose);border-top:3px solid transparent;border-bottom:3px solid transparent;margin-right:5px}
.part-list li small{font-weight:400;color:var(--ink-soft);margin-left:3px}
.news{list-style:none}
.news li{display:flex;align-items:center;gap:6px;height:18px;border-bottom:1px dotted var(--line);font-size:6.5px;padding-left:40px}
.news .tag{background:var(--rose);color:#fff;font-size:5.5px;padding:1px 4px;border-radius:2px}
.news .tag.event{background:var(--green)}
.news .date{color:var(--ink-soft)}
.news-more{display:block;width:100px;margin:10px 0 0 auto;border:1px solid var(--line);border-radius:9px;text-align:center;font-size:6.5px;padding:2px 0;color:var(--ink)}
.request{border:1px solid var(--line);padding:6px;margin-bottom:10px;height:165px;position:relative}
.request h3{font-family:"M PLUS Rounded 1c",sans-serif;font-size:9px;color:var(--rose);line-height:1.3}
.request p{font-size:6px;color:var(--ink-soft);margin-top:4px;width:60px}
.request .person{position:absolute;right:6px;top:10px;width:58px;height:100px;background:linear-gradient(#f4e4e4,#e4c7c7);border-radius:4px}
.request .apply{position:absolute;left:6px;right:6px;bottom:8px;height:24px;background:linear-gradient(#d36a83,var(--rose));border-radius:4px;color:#fff;font-size:9px;font-weight:700;display:flex;align-items:center;justify-content:center}
.award{border:1px solid var(--line);height:150px;padding:6px;margin-bottom:6px;display:flex;flex-direction:column;align-items:center;gap:4px}
.award .prize{width:110px;height:82px;background:linear-gradient(#f7f4ef,#e7dfd2)}
.award p{font-size:7px;text-align:center;font-weight:700;line-height:1.35}
.award p em{font-style:normal;color:var(--rose)}
.banners{display:grid;grid-template-columns:1fr 1fr;gap:4px;margin-bottom:6px}
.banners div{height:40px;border:1px solid var(--line)}
.bn-a{background:linear-gradient(var(--beige),#fff)}
.bn-b{background:linear-gradient(#fbeec8,#f4d98c)}
.bn-c{background:linear-gradient(#e7efdc,#c8d7b2)}
.bn-d{background:linear-gradient(#f6e3e8,#eec3cf)}
.side-bar{height:18px;border:1px solid var(--line);font-size:7px;font-weight:700;display:flex;align-items:center;justify-content:center;margin-bottom:5px}
.side-bar.mail{background:var(--rose);color:#fff;border-color:var(--rose)}
.foot-links{display:grid;grid-template-columns:repeat(4,1fr);gap:3px 8px;list-style:none;padding:12px 20px;margin-top:12px;border-top:1px solid var(--line)}
.foot-links li{font-size:6px;color:var(--ink-soft)}
.foot-links li::before{content:"› ";color:var(--rose)}
.foot-band{background:var(--beige);height:62px;display:flex;align-items:center;justify-content:space-between;padding:0 14px;margin-top:6px}
.foot-band .tel{font-size:15px;justify-content:flex-start}
.foot-band address{font-style:normal;font-size:6px;color:var(--ink-soft);text-align:right;line-height:1.6}
.foot-bottom{background:#6e6462;color:#fff;font-size:6px;height:16px;display:flex;justify-content:space-between;align-items:center;padding:0 10px;margin-top:8px}
</style>
</head>
<body>
<div class="page">
  <header class="header">
    <div class="brand">
      <span class="brand-mark"></span>
      <div>
        <div class="brand-tag">まちの小さな工務店</div>
        <div class="brand-name">株式会社 みのり舎</div>
      </div>
    </div>
    <div class="contact-top">
      <div class="util"><span>資料請求</span><span>お問合せ</span></div>
      <div class="tel">
        <svg width="14" height="14" viewBox="0 0 24 24"><path fill="#c4506b" d="M6.6 10.8a15 15 0 0 0 6.6 6.6l2.2-2.2a1 1 0 0 1 1-.2 11 11 0 0 0 3.6.6 1 1 0 0 1 1 1V20a1 1 0 0 1-1 1A17 17 0 0 1 3 4a1 1 0 0 1 1-1h3.5a1 1 0 0 1 1 1 11 11 0 0 0 .6 3.6 1 1 0 0 1-.3 1z"/></svg>
        0120-482-315
      </div>
      <div class="tel-hours">受付時間 9:00〜18:00（日曜定休）</div>
    </div>
  </header>

  <nav class="nav">
    <a class="current" href="#">ホーム<small>HOME</small></a>
    <a href="#">会社案内<small>COMPANY</small></a>
    <a href="#">施工事例<small>WORKS</small></a>
    <a href="#">お客様の声<small>VOICE</small></a>
    <a href="#">よくある質問<small>Q&amp;A</small></a>
    <a href="#">お問い合わせ<small>CONTACT</small></a>
  </nav>

  <section class="hero">
    <div class="hero-photo" role="img" aria-label="明るいリビングルームの施工写真"></div>
    <div class="hero-band"><span class="lead">まちの小さな工務店</span><span class="sub">全国優秀賞受賞</span></div>
  </section>

  <div class="body">
    <main class="main">
      <div class="sec-head"><h2>リフォーム別ご紹介</h2><span>Reform by house types</span></div>
      <div class="type-grid">
        <article class="type-card"><h3>一般住宅</h3><div class="photo ph-house" role="img" aria-label="一般住宅の室内写真"></div><a class="more">詳しくみる ›</a></article>
        <article class="type-card"><h3>マンション</h3><div class="photo ph-mansion" role="img" aria-label="マンションのキッチン写真"></div><a class="more">詳しくみる ›</a></article>
        <article class="type-card"><h3>新築</h3><div class="photo ph-new" role="img" aria-label="新築住宅の外観写真"></div><a class="more">詳しくみる ›</a></article>
        <article class="type-card"><h3>店舗・商業施設</h3><div class="photo ph-shop" role="img" aria-label="店舗内装の写真"></div><a class="more">詳しくみる ›</a></article>
      </div>

      <div class="sec-head"><h2>部分別リフォームご紹介</h2><span>Reform by parts</span></div>
      <ul class="part-list">
        <li>無垢材<small>FLOORING</small></li>
        <li>珪藻土 塗り壁<small>WALL</small></li>
        <li>キッチン<small>KITCHEN</small></li>
        <li>洗面<small>SANITARY</small></li>
        <li>ユニットバス<small>BATH</small></li>
        <li>トイレ<small>TOILET</small></li>
        <li>クロス<small>CROSS</small></li>
        <li>住宅基礎 ひび割れ補修<small>CRACK</small></li>
        <li>塗装<small>PAINT</small></li>
      </ul>

      <div class="sec-head"><h2>新着情報</h2><span>What's New</span></div>
      <ul class="news">
        <li><span class="tag">お知らせ</span><span class="date">2013.05.23</span>ホームページをリニューアルしました。</li>
        <li><span class="tag event">イベント</span><span class="date">2013.05.20</span>春の住まい相談会を開催します。</li>
        <li><span class="tag">お知らせ</span><span class="date">2013.05.15</span>施工事例を新しく追加しました。</li>
        <li><span class="tag event">イベント</span><span class="date">2013.05.10</span>完成見学会のお知らせです。</li>
        <li><span class="tag">お知らせ</span><span class="date">2013.05.01</span>連休中の営業日についてご案内します。</li>
      </ul>
      <a class="news-more">ニュース一覧へ ›</a>
    </main>

    <aside class="side">
      <div class="request">
        <h3>Webから<br>お問い合わせ<br>資料請求</h3>
        <p>お気軽にご相談ください。</p>
        <div class="person" role="img" aria-label="案内するスタッフの写真"></div>
        <div class="apply">申し込みをする</div>
      </div>
      <div class="award">
        <div class="prize" role="img" aria-label="表彰盾の写真"></div>
        <p>2013年<br><em>全国リフォーム</em><br>優秀賞受賞</p>
      </div>
      <div class="banners">
        <div class="bn-a" role="img" aria-label="リフォーム相談のバナー"></div>
        <div class="bn-b" role="img" aria-label="家づくりのバナー"></div>
        <div class="bn-c" role="img" aria-label="暮らしのアイディアのバナー"></div>
        <div class="bn-d" role="img" aria-label="施工事例のバナー"></div>
      </div>
      <div class="side-bar">2013 みのり舎 施工自慢</div>
      <div class="side-bar mail">✉ メールマガジン登録</div>
    </aside>
  </div>

  <ul class="foot-links">
    <li>施工事例</li><li>会社案内</li><li>お客様の声</li><li>お問い合わせ</li>
    <li>一般住宅</li><li>スタッフ紹介</li><li>よくある質問</li><li>資料請求</li>
    <li>マンション</li><li>アクセス</li><li>メールマガジン</li><li>プライバシー</li>
    <li>新築</li><li>店舗・商業施設</li><li>新着情報</li><li>サイトマップ</li>
  </ul>

  <footer>
    <div class="foot-band">
      <div>
        <div class="brand"><span class="brand-mark"></span><div class="brand-name">株式会社 みのり舎</div></div>
        <div class="tel">0120-482-315</div>
      </div>
      <address>〒980-0000 宮城県仙台市青葉区みのり町1-2<br>TEL 022-555-0142　FAX 022-555-0143<br>http://www.minori-sha.co.jp/</address>
    </div>
    <div class="foot-bottom"><span>個人情報保護方針 ｜ サイトマップ</span><span>Copyright (c) 株式会社 みのり舎 All Rights Reserved.</span></div>
  </footer>
</div>
</body>
</html>
```